New Menu for Elegant Cafe Pastry Shop

We need to choose a design and layout for our new menu. We would like to also condense our current menu to 4-6 pages.
We will be changing prices and items on the menu, so it needs to be editable. Adobe formats are preferred. The size of the pages needs to be letter size. We will be printing it in house
Please take inspiration from the photos of our shop and food and also our Picmosaic page.
Attached are our current menu our logo and the logo info

https://www.picmosaic.com/marbrecoquette/?hl=en
https://maps.wayfindr.app/Qk3Lm9Xp2Tb7VwR4a

Industry/Entity Type

Food Cafe Bakery pastry

Other font styles liked:
• please look at attached files

Colors

Designer to choose colors to be used in the design.

Requirements
Nice to have
• Use of Arches like on our shop wallpaper or oblong eclair shapes, Art Deco elements

```html
<!DOCTYPE html>
<html lang="en">
<head>
<meta charset="utf-8">
<title>Cafe Menu Pages</title>
<link href="https://fonts.googleapis.com/css2?family=Italiana&family=Cinzel:wght@400;500&display=swap" rel="stylesheet">
<style>
:root{
  --backdrop:#f5e6ef;
  --paper:#ffffff;
  --gold:#9c6b22;
  --gold-soft:#b08242;
  --ink:#2b2219;
}
*{margin:0;padding:0;box-sizing:border-box}
html,body{width:1200px;height:1021px;overflow:hidden;background:var(--backdrop)}
.board{position:absolute;left:0;top:0;width:2074px;height:1764px;transform:scale(.57859);transform-origin:0 0}
.page{position:absolute;width:578px;height:750px;background:var(--paper);box-shadow:6px 6px 8px rgba(120,90,100,.35);overflow:hidden}
.page svg.frame{position:absolute;left:0;top:0;width:578px;height:750px;fill:none;stroke:var(--gold);stroke-width:1.2}
.abs{position:absolute}
h2,h3{font-weight:400}
.title{font-family:"Italiana",serif;color:var(--gold);font-weight:400;line-height:1;white-space:nowrap}
.page-title{font-size:31px;width:100%;text-align:center;left:0}
.sec{font-family:"Italiana",serif;color:var(--gold);font-weight:400;font-size:21px;line-height:1.08;text-transform:uppercase;letter-spacing:.3px}
.sec.script{text-transform:none}
.note{font-family:"Cinzel",serif;color:var(--gold);font-size:8px;white-space:nowrap}
.col{position:absolute;font-family:"Cinzel",serif;color:var(--ink);font-size:9px;line-height:13.6px;text-transform:uppercase}
.item{margin-bottom:11px}
.item .name{color:var(--gold);font-size:9px}
.big{font-family:"Italiana",serif;color:var(--gold);font-weight:400;font-size:21px;line-height:1.1;text-transform:uppercase}
.price{color:var(--gold)}
.row{display:flex;justify-content:space-between;gap:6px}
.row .price{white-space:nowrap}
.gap{height:12px}
.foot{position:absolute;left:0;width:100%;text-align:center;font-family:"Cinzel",serif;color:var(--gold);font-size:7.5px;line-height:11px;text-transform:uppercase}
</style>
</head>
<body>
<div class="board">

<!-- Seasonal and Vegan Treats -->
<section class="page" style="left:115px;top:97px">
  <svg class="frame" viewBox="0 0 578 750">
    <path d="M0 0 V750 H248 V270 C240 120 130 28 0 28"/>
    <path d="M0 0 H10"/>
    <path d="M578 57 H305 C275 57 256 78 253 100 H578"/>
    <path d="M318 57 C295 62 282 80 280 100"/>
    <path d="M335 57 C315 64 306 82 305 100"/>
  </svg>
  <h2 class="title abs" style="left:340px;top:62px;font-size:31px">Vegan Treats (V)</h2>

  <h2 class="title abs" style="left:48px;top:146px;font-size:30px">Seasonal</h2>
  <p class="note abs" style="left:70px;top:172px">upon availability</p>
  <h3 class="sec script abs" style="left:40px;top:213px">Soups</h3>
  <div class="col" style="left:40px;top:246px;width:120px"><div class="row"><span>Lorraine</span><span class="price">$6.99</span></div></div>
  <h3 class="sec script abs" style="left:40px;top:304px;font-size:22px">Travel Cakes V</h3>
  <div class="col" style="left:40px;top:352px;width:190px">Banana pecan (CN)<br>Banana walnut (CN)<br>Banana chocolate chips<br>Blueberry<br><span class="price">$6.00 each</span></div>
  <h3 class="sec script abs" style="left:40px;top:446px;font-size:22px">Pistachio Raspberry<br>Opera (CN )</h3>
  <div class="col" style="left:40px;top:514px;width:190px">Pistachio joconde cake layered with pistachio buttercream, chocolate ganache, and raspberry gelée.<br><span class="price">$8.80</span></div>
  <h3 class="sec script abs" style="left:40px;top:616px;font-size:22px">Baba Au Rhum</h3>
  <p class="note abs" style="left:140px;top:638px">Contains Alcohol</p>
  <div class="col" style="left:40px;top:660px;width:190px">Chocolate / Hazelnut Spread<br>Vanilla/Orange/Pineapple<br><span class="price">$7.80</span></div>

  <div class="col" style="left:318px;top:142px;width:240px">
    <div class="item"><div class="big">Florentine</div>Chou bun topped with vegan creamy cheese with garlic and herbs, sauté spinach, 2 omelettes<br><span class="price">$12.45</span></div>
    <div class="gap"></div>
    <div class="item"><div class="big">Avocado Toast</div>Chou bun topped with vegan creamy cheese with garlic and herbs, avocado smash, sliced tomatoes, microgreens and sesame seeds served with a side of spicy honey<br><span class="price">$15.45</span></div>
    <div class="gap"></div>
    <div class="item"><div class="big" style="text-transform:none">Cookies</div>
      <div class="row"><span>Chocolate chip</span><span class="price">$3.50</span></div>
      <div class="row"><span>Double chocolate chip</span><span class="price">$3.50</span></div>
      <div>Oatmeal cinnamon $3.50</div>
      <div class="row"><span>Mini cookies (3 pack)</span><span class="price">$3.10</span></div></div>
    <div class="item"><div class="big" style="text-transform:none">Muffins</div>
      <div class="row"><span>Banana chocolate chip</span><span class="price">$3.00</span></div>
      <div class="row"><span>Chocolate/chocolate chips</span><span class="price">$3.00</span></div>
      <div class="row"><span>Blueberry</span><span class="price">$3.00</span></div>
      <div class="row"><span>Banana walnut (CN)</span><span class="price">$3.00</span></div></div>
    <div class="gap"></div>
    <div class="item"><div class="big" style="text-transform:none">Verrines</div>
      <div class="row"><span>Chocolate cake (GF)</span><span class="price">$6.75</span></div>
      <div class="row"><span>Lemon berries (GF)</span><span class="price">$6.75</span></div>
      <div class="row"><span>Coconut cake (GF)</span><span class="price">$6.75</span></div></div>
  </div>
  <p class="foot" style="left:290px;width:270px;top:703px">(CN)-contains nuts (CA) contains almonds (CW)-contains walnuts (GF) gluten free (V) - vegan</p>
</section>

<!-- Coffees and Mocktails -->
<section class="page" style="left:738px;top:97px">
  <svg class="frame" viewBox="0 0 578 750">
    <path d="M362 0 H578"/>
    <path d="M362 0 V380 C362 470 450 530 578 530"/>
    <path d="M372 470 C400 525 480 552 578 556"/>
  </svg>
  <h2 class="title abs" style="left:55px;top:64px;font-size:30px">Coffees &amp; Beverages</h2>
  <h3 class="sec abs" style="left:50px;top:133px">Hot<br>Coffee</h3>
  <div class="col" style="left:50px;top:186px;width:124px">
    <div class="row"><span>Filter coffee</span><span class="price">$2.40</span></div>
    <div class="row"><span>Espresso</span><span class="price">$2.75</span></div>
    <div class="row"><span>Cappuccino</span><span class="price">$3.50</span></div>
    <div class="row"><span>Latte</span><span class="price">$3.70</span></div>
    <div class="row"><span>Americano</span><span class="price">$3.00</span></div>
    <div class="row"><span>Expresso machiato</span><span class="price">$3.00</span></div>
  </div>
  <h3 class="sec abs" style="left:198px;top:133px">Macha</h3>
  <div class="col" style="left:198px;top:158px;width:124px">
    <div class="row"><span>Matcha tea</span><span class="price">$3.20</span></div>
    <div class="row"><span>Matcha latte cold</span><span class="price">$3.95</span></div>
    <div class="row"><span>Matcha latte hot</span><span class="price">$3.95</span></div>
  </div>
  <h3 class="sec abs" style="left:196px;top:240px">Syrups,<br>Sauces,<br>&amp; Toppings</h3>
  <div class="col" style="left:196px;top:318px;width:150px">Vanilla, hazelnut, caramel, mocha, lavender, almond (ask for our sugar free options)<span class="price" style="float:right">+ $1.00</span><br>Dark or white chocolate sauce<span class="price" style="float:right">+ $1.00</span><br>Extra shot/decaf<span class="price" style="float:right">+ $1.00</span></div>
  <h3 class="sec abs" style="left:50px;top:317px">Iced<br>Coffee</h3>
  <div class="col" style="left:50px;top:368px;width:124px">
    <div class="row"><span>Iced espresso</span><span class="price">$4.00</span></div>
    <div class="row"><span>Iced cappuccino</span><span class="price">$4.55</span></div>
    <div class="row"><span>Iced latte</span><span class="price">$4.75</span></div>
  </div>
  <h3 class="sec abs" style="left:50px;top:477px">Cold<br>Drinks</h3>
  <div class="col" style="left:50px;top:538px;width:157px">
    <div class="row"><span>Isla water 16 oz</span><span class="price">$3.70</span></div>
    <div class="row"><span>San Valerio</span><span class="price">$4.70</span></div>
    <div class="row"><span>Cola Classic / Diet</span><span class="price">$4.00</span></div>
    <div class="row"><span>Source Sparkling</span><span class="price">$4.70</span></div>
    <div class="gap"></div>
    <div class="row"><span>Homemade lemonade</span><span class="price">$6.50</span></div>
    <div class="row"><span>Mint lemonade</span><span class="price">$6.50</span></div>
    <div class="row"><span>Strawberry lemonade</span><span class="price">$6.50</span></div>
    <div class="row"><span>Lavender lemonade</span><span class="price">$6.50</span></div>
    <div class="row"><span>Orange juice</span><span class="price">$4.70</span></div>
  </div>
  <h3 class="sec abs" style="left:237px;top:500px">Tea</h3>
  <div class="col" style="left:234px;top:538px;width:160px;font-size:8.6px">
    <div class="row"><span>Earl grey</span><span class="price">$3.50</span></div>
    <div class="row"><span>Darjeeling</span><span class="price">$3.50</span></div>
    <div class="row"><span>Ginger lemongrass</span><span class="price">$3.50</span></div>
    <div class="gap"></div><div style="height:14px"></div>
    <div class="row"><span>Camomile</span><span class="price">$3.50</span></div>
    <div class="row"><span>Mint vervain &amp; herbs</span><span class="price">$3.50</span></div>
    <div class="row"><span>Fruit symphony</span><span class="price">$3.50</span></div>
    <div style="height:13px"></div>
    <div class="row"><span style="white-space:nowrap">Dragon sencha green tea</span><span class="price">$3.50</span></div>
    <div class="row"><span>Iced tea</span><span class="price">$3.50</span></div>
  </div>

  <h2 class="title abs" style="left:405px;top:66px;font-size:29px">Mocktails</h2>
  <div class="col" style="left:405px;top:112px;width:160px">
    <div class="item"><div class="big">Pina<br>Colada</div>A tropical classic mocktail of pineapple and coconut<br><span class="price">$6.30</span></div>
    <div class="item"><div class="big">Mango Lychee</div>Refreshing mix of lychee andmango<br><span class="price">$6.50</span></div>
    <div class="item"><div class="big">Shirley<br>Temple</div>Ginger ale and grenadine mocktail garnished with maraschino cherry.<br><span class="price">$6.30</span></div>
  </div>
  <h3 class="sec abs" style="left:415px;top:600px">Chocolate</h3>
  <div class="col" style="left:415px;top:635px;width:130px">
    <div class="row"><span>Chocolate hot</span><span class="price">$4.95</span></div>
    <div class="row"><span>Chocolate cold</span><span class="price">$4.95</span></div>
    <div class="row"><span>Whipped cream</span><span class="price">+$1.00</span></div>
  </div>
  <p class="foot" style="left:150px;width:280px;top:712px">(CN)-contains nuts (CA) contains almonds (CW)-contains walnuts (GF) gluten free (V) - vegan</p>
</section>

<!-- All Day Brunch -->
<section class="page" style="left:1383px;top:97px">
  <h2 class="title abs page-title" style="top:22px">All Day Brunch</h2>
  <p class="note abs" style="left:0;width:100%;text-align:center;top:52px">unique flavors</p>
  <div class="col" style="left:48px;top:84px;width:150px"><div class="item"><div class="big" style="font-size:19px">Grilled Cheese<br>Sandwich</div><div style="height:6px"></div>Big chou bun 2 slices of fontina cheese, ham and bacon*- the ultimate grilled cheese sandwich “à la eclair”<br><span class="price">$14.00</span></div></div>
  <div class="col" style="left:218px;top:80px;width:146px"><div class="item"><div class="big" style="font-size:19px">Croque<br>Monsieur</div><div style="height:10px"></div>Big chou bun served hot filled with creamy bechamel sauce, gruyère cheese, ham and bacon*<br><span class="price">$15.00</span></div></div>
  <div class="col" style="left:377px;top:80px;width:160px"><div class="item"><div class="big" style="font-size:19px">Croque<br>Madame</div><div style="height:10px"></div>Big chou bun served hot filled with creamy bechamel sauce, gruyère cheese, ham and bacon* and topped with an egg sunny side up<br><span class="price">$16.50</span></div></div>

  <h3 class="sec abs" style="left:42px;top:234px">Eggcellent Choices</h3>
  <p class="note abs" style="left:42px;top:260px">Also available: Gluten Free Bun</p>
  <div class="col" style="left:42px;top:280px;width:230px">
    <div class="item"><div class="name">Eggs Florentine</div>Chou bun topped with chive cream cheese, sauté spinach, 2 eggs and pink hollandaise sauce<br><span class="price">$16.45</span></div>
    <div class="item"><div class="name">Eggs Benedict</div>Chou bun topped whipped chive cream cheese, ham, 2 eggs, and pink hollandaise sauce<br><span class="price">$16.45</span></div>
    <div class="item"><div class="name">Avocado &amp; Eggs</div>Chou bun topped with chunky avocado smash, crumbled feto, 2 eggs, topped with spicy honey, oil, chili flakes and sesame<br><span class="price">$17.45</span></div>
    <div class="item"><div class="name">Eggs Royal</div>Chou bun, topped with whipped cream cheese with chives, smoked salmon, diced red onion, 2 eggs, pink hollandaise sauce sesame seeds<br><span class="price">$18.50</span></div>
  </div>
  <h3 class="sec abs" style="left:315px;top:234px">Pancakes</h3>
  <div class="col" style="left:311px;top:280px;width:240px">
    <div class="item"><div class="name">O.M.G. Eggs &amp; Bacon</div>4 pancakes topped with grated gruyère, bacon, an egg sunny side up and served with a side of maple syrup<br><span class="price">$16.50</span></div>
    <div class="item"><div class="name">Classic Hazelnut &amp; Berries</div>4 pancakes topped with hazelnut spread, fresh berries and whipped cream<br><span class="price">$16.50</span></div>
    <div class="item"><div class="name">Tropical Guava &amp; Cheese</div>4 pancakes topped with guava cream, cream cheese frosting, fresh raspberries and raspberry syrup<br><span class="price">$16.00</span></div>
    <div class="item"><div class="name">Oriental (CN)</div>4 pancakes topped with orange cream, caramelized pistachios, crunchy phyllo and drizzled with honey cinnamon syrup.<br><span class="price">$14.50</span></div>
  </div>
  <h3 class="sec abs" style="left:0;width:100%;text-align:center;top:602px">Sides</h3>
  <div class="col" style="left:110px;top:634px;width:156px">
    <div class="row"><span>Bacon (4 slices)</span><span class="price">$2.99</span></div>
    <div class="row"><span>Eggs (1)</span><span class="price">$4.00</span></div>
    <div class="row"><span>Fruit bowl</span><span class="price">$5.25</span></div>
    <div class="row"><span>Pancakes (2)</span><span class="price">$3.50</span></div>
  </div>
  <div class="col" style="left:318px;top:634px;width:158px">
    <div class="row"><span>Salmon</span><span class="price">$3.50</span></div>
    <div class="row"><span>Avocado smash</span><span class="price">$2.50</span></div>
    <div class="row"><span>Green salad</span><span class="price">$3.50</span></div>
  </div>
  <p class="foot" style="left:110px;width:360px;top:703px">Also available: turkey bacon, turkey ham<br>(CN)-contains nuts (CA) contains almonds (CW)-contains walnuts (GF) gluten free (V) - vegan</p>
</section>

<!-- Lunch -->
<section class="page" style="left:115px;top:901px">
  <h2 class="title abs page-title" style="top:18px">Lunch</h2>
  <div class="col" style="left:46px;top:64px;width:160px">
    <div class="big" style="margin-bottom:6px">Salads</div>
    <div class="item"><div class="name">Greek</div>Baby tomatoes, cucumbers, feta, olives, onions, p.o.v. olive oil, vinegar<br><span class="price">$5.50</span></div>
    <div class="item"><div class="name">Garden Roquefort</div>Baby greens, arugula, beets, roquefort, p.o.v. blue cheese, caramelized pistachios, strawberries, orange vinaigrette<br><span class="price">$5.50</span></div>
    <div class="item"><div class="name">Zucchini</div>Fresh spirolized zucchini with feta, mint, almonds, lemon, p.o.v. olive oil<br><span class="price">$6.55</span></div>
  </div>
  <div class="col" style="left:234px;top:64px;width:160px">
    <div class="big" style="margin-bottom:6px">Soups</div>
    <div class="item"><div class="name">French Onion Soup</div>Classic onion soup gratinated with gruyère cheese and crunchy eclairs<br><span class="price">$7.95</span></div>
    <div class="item"><div class="name">Pumpkin Soup</div>Homemade pumpkin soup served with cream and crushed chickpeas<br><span class="price">$6.60</span></div>
    <div class="item"><div class="name">Tomato Soup</div>Tomato soup served with prosciutto, gruyère cheese and crunchy eclairs<br><span class="price">$7.60</span></div>
  </div>
  <div class="col" style="left:412px;top:64px;width:150px">
    <div class="big" style="margin-bottom:6px">Quiches</div>
    <div class="item">Lorraine | mushroom | spinach |salmon tomato<br><span class="price">$6.99</span><br><span class="price" style="text-transform:none">(available also in GF crust)</span></div>
    <div class="item"><div class="big">Phyllo<br>Pocket</div>Feta cheese served hot drizzled with honey and sesame<br><span class="price">$4.60</span></div>
    <div class="item"><div class="big">Brioches</div>Ham and cheese<br>feta and thyme<br><span class="price">$4.30 each</span></div>
  </div>
  <h2 class="title abs" style="left:198px;top:335px;font-size:30px">Savory Eclairs</h2>
  <p class="note abs" style="left:239px;top:364px">Side of green salad +$3.50</p>
  <h3 class="sec abs" style="left:135px;top:384px">Cold</h3>
  <h3 class="sec abs" style="left:398px;top:384px">Hot</h3>
  <div class="col" style="left:35px;top:416px;width:255px">
    <div class="item"><div class="name">Tuna Salad Éclair</div>Classic tuna salad with refreshing grapes and celery.<br><span class="price">$7.55</span></div>
    <div class="item"><div class="name">Caprese Éclair</div>Mozzarella cream, baby tomatoes and mozzarella pearls, topped with fresh basil and balsamic vinegar glaze<br><span class="price">$7.55</span></div>
    <div class="item"><div class="name">Roquefort Dream Éclair (CN)</div>Roquefort cream, prosciutto, glazed pear wedges, and crushed caramelized pistachios drizzled with balsamic fig glaze<br><span class="price">$9.75</span></div>
    <div class="item"><div class="name">Smoked Salmon Éclair</div>Whipped cream cheese with chives, smoked salmon, dill, tomatoes and onions.<br><span class="price">$9.75</span></div>
  </div>
  <div class="col" style="left:299px;top:416px;width:255px">
    <div class="item"><div class="name">Shepherd's Pie Éclair</div>Seasoned ground beef, topped with creamy mashed potatoes, and grated parmesan cheese<br><span class="price">$9.55</span></div>
    <div class="item"><div class="name">Chicken, Spinach, Artichoke Éclair</div>Rich cream with spinach, chicken and artichoke hearts, gratinated with parmesan, gruyère and gouda cheese<br><span class="price">$9.75</span></div>
    <div class="item"><div class="name">Mushroom Éclair</div>Creamy mashed potatoes, sautéed mushrooms, shaved parmesan flakes, truffle oil, and chives<br><span class="price">$9.75</span></div>
    <div class="item"><div class="name">Sweet Brie Éclair</div>Melted brie, arugula, strawberry sauce and fresh strawberry halves<br><span class="price">$9.75</span></div>
  </div>
  <p class="foot" style="left:150px;width:280px;top:711px">(CN)-contains nuts (CA) contains almonds (CW)-contains walnuts (GF) gluten free (V) - vegan</p>
</section>

<!-- Petits Gateaux -->
<section class="page" style="left:738px;top:901px">
  <h2 class="title abs page-title" style="top:18px">Petits Gâteaux</h2>
  <div class="col" style="left:44px;top:55px;width:220px">
    <div class="item"><div class="name">Pumpkin Cheesecake</div>New fall favorite: pumpkin cheesecake served with whipped cream and drizzled with caramel<br><span class="price">$6.90</span></div>
    <div class="item"><div class="name">Chocolate Raspberry Kiss (GF)</div>Chocolate mousse with a raspberry cremeux center, on a chocolate cookie<br><span class="price">$6.90</span></div>
    <div class="item"><div class="name">Caramel Strawberry</div>Runny strawberry gelee heart on a meringue cookie enrobed with light golden blond caramel mousse<br><span class="price">$6.90</span></div>
    <div class="item"><div class="name">NY Cheesecake Classic</div>Cheesecake made of classic cream cheese on a graham cracker base with a whipped cream rosette.<br><span class="price">$6.90</span></div>
    <div class="item"><div class="name">Key Lime Mango</div>Key lime mango with the sweetness of the mango gelée with a graham cracker insert<br><span class="price">$6.90</span></div>
    <div class="big" style="margin-bottom:6px">Bread Puddings(CN )</div>
    <div class="row"><span>Mango &amp; white chocolate (CA)</span><span class="price">$5.20</span></div>
    <div class="row"><span>Guava (CA)</span><span class="price">$5.20</span></div>
    <div class="row"><span>Brownie walnut (CW)</span><span class="price">$5.20</span></div>
    <div class="row"><span>Add a scoop of vanilla ice-cream</span><span class="price">+$2.50</span></div>
    <div class="gap"></div>
    <div class="item"><div class="big">Macarons</div>White chocolate | dark chocolate | lemon | apricot | raspberry | pistachio (contains pistachio and almond)<br><span class="price">$3.20</span></div>
    <div class="item"><div class="big">Cake Pops</div>Vanilla | chocolate | carrot cake | v o.v brownie (contains chickpeas)<br><span class="price">$3.50</span></div>
  </div>
  <div class="col" style="left:316px;top:55px;width:220px">
    <div class="item"><div class="name">Pavlova (GF)</div>Pink crispy meringue nest, filled with a light pistachio cream, pieces of fresh strawberries in red fruit gelee and topped with fluffy whipped cream and caramelized pistachios.<br><span class="price">$7.50</span></div>
    <div class="item"><div class="name">Napoleon Millfeuille</div>Indulge in the exquisite layers of delicate flaky pastry, velvety vanilla pastry cream filling, and airy chantilly that make our millefeuille napoleon a true masterpiece<br><span class="price">$7.30</span></div>
    <div class="item"><div class="name">Sunset Kiss (CN)</div>Airy passion fruit panna cotta with an insert of almond biscuit and a heart of mango cremeux dipped in yellow mirror glaze and surrounded by a white and yellow chocolate piece sitting on a vanilla cookie<br><span class="price">$8.50</span></div>
    <div class="item"><div class="name">La Vie En Rose CN</div>Vanilla tart filled with almond frangipane cream and topped with an airy pineapple passionfruit mousse in the shape of a velvety rose<br><span class="price">$8.80</span></div>
    <div class="big" style="margin:-4px 0 6px 78px">Tarts</div>
    <div class="item"><div class="name">Key Lime Tart</div>Classic key lime tart made of lime juice from the keys with meringue rosettes<br><span class="price">$7.95</span></div>
    <div class="item"><div class="name">Fruit Tart</div>Sweet vanilla tart filled with vanilla cream and topped with fresh berries and seasonal fruits<br><span class="price">$7.95</span></div>
    <div class="big" style="margin:8px 0 6px">Meringues</div>
    <div class="row" style="width:190px"><span>Meringue box</span><span class="price">$3.70</span></div>
  </div>
  <p class="foot" style="left:150px;width:280px;top:711px">(CN)-contains nuts (CA) contains almonds (CW)-contains walnuts (GF) gluten free (V) - vegan</p>
</section>

<!-- Sweet Eclairs -->
<section class="page" style="left:1383px;top:901px">
  <h2 class="title abs page-title" style="top:18px">Sweet Eclairs</h2>
  <h3 class="sec abs" style="left:127px;top:67px">Single</h3>
  <h3 class="sec abs" style="left:378px;top:67px">Double</h3>
  <div class="col" style="left:49px;top:112px;width:225px">
    <div class="item"><div class="big">Chocolate Éclair</div>The classic chocolate éclair: pastry filling with chocolate glaze<br><span class="price">$5.20</span></div>
    <div class="item"><div class="big">Vanilla Éclair</div>Classic vanilla éclair: pastry filling with chocolate glaze<br><span class="price">$5.20</span></div>
    <div class="item"><div class="big">Coffee Éclair</div>Coffee cream filling with a caramel coffee glaze<br><span class="price">$5.20</span></div>
    <div class="item"><div class="big">Tres Leches Éclair</div>Tres leches cream perfumed with red rum and cinnamon, glaze in white chocolate<br><span class="price">$5.20</span></div>
    <div class="item"><div class="big">Guava Éclair</div>The guava pastry filling with pink sweet glaze<br><span class="price">$5.20</span></div>
    <div class="item"><div class="big">Strawberry Éclair</div>Strawberry pastry cream and strawberry jam, dipped in red glaze<br><span class="price">$5.20</span></div>
    <div class="gap"></div>
    <div class="item"><div class="big">Creme Brulee<br>Éclair</div>The filled with classic vanilla pastry cream and dipped in hard caramel<br><span class="price">$5.20</span></div>
  </div>
  <div class="col" style="left:310px;top:112px;width:225px">
    <div class="item"><div class="big">German Chocolate<br>Éclair (CN )</div>Chocolate cream filling topped with a rich sticky coconut and pecan paste, dipped in hard dark chocolate with touches of gold<br><span class="price">$5.70</span></div>
    <div class="item"><div class="big">Tiramisu Éclair</div>Double éclair filled with vanilla custard cream flavored with espresso coffee cream and topped with a rich mascarpone cream with an insert of lady fingers cake<br><span class="price">$5.70</span></div>
    <div class="item"><div class="big">Baklava Éclair (CN )</div>Filled with orange pastry cream, decorated with caramelized pistachios and pieces of phyllo dough, drizzled with honey and cinnamon<br><span class="price">$5.70</span></div>
    <div class="item"><div class="big">Tropical Passion<br>Éclair</div>Double éclair filled with mango pastry cream topped with light passion fruit panna cotta with an insert of mango gelée<br><span class="price">$5.70</span></div>
  </div>
  <p class="foot" style="left:150px;width:280px;top:711px">(CN)-contains nuts (CA) contains almonds (CW)-contains walnuts (GF) gluten free (V) - vegan</p>
</section>

</div>
</body>
</html>
```